Packiging of Dietry Supplemnts - New Swiss Style Design

please make upgraded design from the attched design .
www.lorvinta.com

Target Market(s)

Switzerland & USA

Industry/Entity Type

Vitamins

Font styles to use
Sans Serif

Colors
0054AA
0677BA
7BADD7
CADEEF
E8F1F8
EB3D1F
EC4F4E
F09395
F8D3D4
FCEDEE

Requirements
Must have
• Swiss Style
Should not have
• dont use the old design style or photo

```html
<!DOCTYPE html>
<html lang="en">
<head>
<meta charset="utf-8">
<title>Collagen Sachet Cartons – Swiss Style Dielines</title>
<link href="https://fonts.googleapis.com/css2?family=Inter:wght@400;500;700;800&display=swap" rel="stylesheet">
<style>
  :root{
    --ink:#1d1d1f;
    --paper:#ffffff;
    --cut:#c9c9c9;
    --blue-900:#0054AA; --blue-700:#0677BA; --blue-400:#7BADD7; --blue-200:#CADEEF; --blue-100:#E8F1F8;
    --red-700:#EB3D1F; --red-600:#EC4F4E; --red-400:#F09395; --red-200:#F8D3D4; --red-100:#FCEDEE;
  }
  *{box-sizing:border-box;margin:0;padding:0}
  html,body{width:1200px;height:789px;overflow:hidden;background:var(--paper)}
  body{font-family:"Inter",Arial,sans-serif;color:var(--ink);position:relative}

  /* ---------- dieline frame ---------- */
  .dieline{position:absolute;top:270px;width:392px;height:250px}
  .dieline--derma{left:4px;--main:var(--blue-900);--tint:var(--blue-400);--soft:var(--blue-200);--pale:var(--blue-100);--accent:var(--red-700)}
  .dieline--hair{left:404px;--main:var(--red-700);--tint:var(--red-400);--soft:var(--red-200);--pale:var(--red-100);--accent:var(--blue-900)}
  .dieline--joints{left:804px;--main:var(--blue-700);--tint:var(--blue-400);--soft:var(--blue-200);--pale:var(--blue-100);--accent:var(--red-600)}

  .panel{position:absolute;overflow:hidden}
  .flap{position:absolute;border:0.6px solid var(--cut);background:var(--pale)}
  .glue-left{left:0;top:70px;width:16px;height:108px;border-radius:3px 0 0 3px}
  .glue-right{left:386.5px;top:70px;width:5px;height:108px}
  .tuck{width:48px;height:7px;background:var(--soft);border:none}
  .tuck-a{left:150.5px;top:26px;border-radius:4px 4px 0 0}
  .tuck-b{left:336px;top:26px;border-radius:4px 4px 0 0}
  .tuck-c{left:150.5px;top:217.5px;border-radius:0 0 4px 4px}
  .tuck-d{left:336px;top:217.5px;border-radius:0 0 4px 4px}

  .brand{font-weight:700;letter-spacing:-.1px;display:inline-flex;align-items:center;gap:.3em;white-space:nowrap}
  .brand .mark{width:.6em;height:.6em;background:var(--accent);display:inline-block}

  /* ---------- lid ---------- */
  .lid{left:15.5px;top:0;width:132.5px;height:68.5px;background:var(--main)}
  .lid .brand{position:absolute;left:7px;bottom:7px;transform:rotate(180deg);transform-origin:center;color:#fff;font-size:7px;right:7px;justify-content:flex-end}
  .lid .rule{position:absolute;left:7px;right:7px;top:7px;height:.6px;background:rgba(255,255,255,.5)}

  /* ---------- front faces ---------- */
  .face{top:68.5px;width:132.5px;height:111.5px;background:var(--paper);border-top:.6px solid var(--cut)}
  .face-1{left:15.5px}
  .face-2{left:201px}
  .face .brand{position:absolute;left:7px;top:6px;font-size:6px;color:var(--ink)}
  .face .block{position:absolute;right:0;top:0;width:30px;height:30px;background:var(--main)}
  .face .block::after{content:"";position:absolute;left:0;bottom:0;width:10px;height:10px;background:var(--accent)}
  .face .range{position:absolute;left:7px;top:17px;font-size:8.5px;font-weight:500;color:var(--main);white-space:nowrap}
  .face .range sup{font-size:4px;vertical-align:top;font-weight:400}
  .face .name{position:absolute;left:6.5px;top:26px;font-size:19px;font-weight:800;letter-spacing:-.8px;line-height:1;color:var(--ink)}
  .face .rule{position:absolute;left:7px;right:7px;top:48px;height:.7px;background:var(--ink)}
  .face .lead{position:absolute;left:7px;top:51px;font-size:4.6px;color:var(--ink)}
  .face .claim{position:absolute;left:7px;top:57px;font-size:6.8px;font-weight:700;color:var(--main);white-space:nowrap}
  .face .ingr{position:absolute;left:7px;right:7px;top:67px;font-size:3.5px;line-height:1.35;color:var(--ink)}
  .face .weight{position:absolute;left:7px;top:79px;font-size:3.3px;line-height:1.3}
  .face .band{position:absolute;left:0;right:0;bottom:0;height:19px;background:var(--main);color:#fff;padding:4px 7px;display:flex;justify-content:space-between;align-items:flex-start}
  .face .band .format{font-size:4.2px;font-weight:700;line-height:1.3;letter-spacing:.2px}
  .face .band .format span{display:block;font-weight:400;letter-spacing:0}
  .face .band .count{font-size:5.5px;font-weight:800}

  /* ---------- side panels ---------- */
  .side{top:32.5px;width:53px;height:185px;background:var(--main);color:#fff;padding:40px 4px 4px;font-size:2.6px;line-height:1.35;display:flex;flex-direction:column;gap:1.6px}
  .side-a{left:148px}
  .side-b{left:333.5px}
  .side h4{font-size:2.9px;font-weight:700;border-top:.4px solid rgba(255,255,255,.6);padding-top:1.2px}
  .side ul{list-style:none}
  .side li{padding-left:2px;position:relative}
  .side li::before{content:"";position:absolute;left:0;top:1.2px;width:.8px;height:.8px;background:#fff}
  .comp{background:#fff;color:var(--ink);font-size:2.3px;border-collapse:collapse;width:100%}
  .comp caption{background:#fff;color:var(--main);font-weight:700;font-size:2.5px;padding:.8px;text-align:left}
  .comp th{background:var(--soft);font-weight:700;padding:.6px;text-align:left}
  .comp td{border-top:.3px solid var(--soft);padding:.6px}
  .side .foot{margin-top:auto;display:flex;flex-direction:column;gap:1px}
  .side .foot .brand{font-size:5px;color:#fff}
  .side .foot small{font-size:2.2px}

  /* ---------- bottom ---------- */
  .bottom{left:201px;top:180px;width:132.5px;height:67.5px;background:var(--main);color:#fff}
  .bottom .brand{position:absolute;left:7px;top:14px;font-size:8px;color:#fff}
  .batch{position:absolute;left:64px;top:10px;width:61.5px;height:18px;background:#fff;color:var(--ink);font-size:2.7px;font-weight:700;padding:2px 3px;line-height:1.45}
  .maker{position:absolute;left:64px;top:33px;font-size:2.5px;font-weight:500;line-height:1.35}
</style>
</head>
<body>

<!-- ========== DERMIA ========== -->
<section class="dieline dieline--derma" aria-label="Dermia Collagen carton dieline">
  <div class="flap glue-left"></div><div class="flap glue-right"></div>
  <div class="flap tuck tuck-a"></div><div class="flap tuck tuck-b"></div><div class="flap tuck tuck-c"></div><div class="flap tuck tuck-d"></div>
  <div class="panel lid"><span class="rule"></span><span class="brand"><i class="mark"></i>Lorvinta</span></div>

  <div class="panel face face-1">
    <span class="block"></span>
    <span class="brand"><i class="mark"></i>Lorvinta</span>
    <div class="range">Dermia<sup>®</sup></div>
    <div class="name">Collagen</div>
    <span class="rule"></span>
    <div class="lead">Helps in Maintaining</div>
    <div class="claim">Healthy Skin</div>
    <div class="ingr">Hydrolyzed Collagen, Sodium Hyaluronate,<br>Biotin &amp; Coenzyme Q10</div>
    <div class="weight">(7 sachets of 14.5 g)<br>Net weight: 101.5 g</div>
    <div class="band"><div class="format">POWDER IN SACHETS<span>Food Supplement</span></div><div class="count">7 Sachets</div></div>
  </div>

  <div class="panel side side-a">
    <p><b>Dermia Collagen</b> is a daily blend of collagen peptides with nutrients for skin.</p>
    <table class="comp"><caption>Composition</caption>
      <tr><th>Ingredients</th><th>Per Sachet</th></tr>
      <tr><td>Collagen</td><td>10000 mg</td></tr>
      <tr><td>Vitamin C</td><td>80 mg</td></tr>
      <tr><td>Biotin</td><td>50 µg</td></tr>
    </table>
    <p><b>Ingredients:</b> Bovine Collagen, Vitamin C, Biotin, Flavour.</p>
    <div class="foot"><span class="brand"><i class="mark"></i>Lorvinta</span><small>www.lorvinta.com</small></div>
  </div>

  <div class="panel face face-2">
    <span class="block"></span>
    <span class="brand"><i class="mark"></i>Lorvinta</span>
    <div class="range">Dermia<sup>®</sup></div>
    <div class="name">Collagen</div>
    <span class="rule"></span>
    <div class="lead">Helps in Maintaining</div>
    <div class="claim">Healthy Skin</div>
    <div class="ingr">Hydrolyzed Collagen, Sodium Hyaluronate,<br>Biotin &amp; Coenzyme Q10</div>
    <div class="weight">(7 sachets of 14.5 g)<br>Net weight: 101.5 g</div>
    <div class="band"><div class="format">POWDER IN SACHETS<span>Food Supplement</span></div><div class="count">7 Sachets</div></div>
  </div>

  <div class="panel bottom">
    <span class="brand"><i class="mark"></i>Lorvinta</span>
    <div class="batch">Batch No.:<br>MFG. Date<br>EXP. Date</div>
    <div class="maker">Velmora S.r.l. Via Orsini 12<br>20121 Milano (MI) - Italy</div>
  </div>

  <div class="panel side side-b">
    <h4>Directions for use:</h4>
    <ul><li>For adults only.</li><li>Take 1 sachet per day, or as directed by the healthcare provider.</li><li>Dissolve the sachet into a glass of water (250 ml).</li></ul>
    <h4>Precautions:</h4>
    <ul><li>Do not exceed the recommended daily dose.</li><li>Not a substitute for a varied, balanced diet.</li><li>Do not use after the expiry date.</li></ul>
    <h4>Storage conditions:</h4>
    <ul><li>Store in a cool (&lt;25°C) and dry place.</li><li>Keep out of reach of children.</li></ul>
  </div>
</section>

<!-- ========== CAPILLA ========== -->
<section class="dieline dieline--hair" aria-label="Capilla Collagen carton dieline">
  <div class="flap glue-left"></div><div class="flap glue-right"></div>
  <div class="flap tuck tuck-a"></div><div class="flap tuck tuck-b"></div><div class="flap tuck tuck-c"></div><div class="flap tuck tuck-d"></div>
  <div class="panel lid"><span class="rule"></span><span class="brand"><i class="mark"></i>Lorvinta</span></div>

  <div class="panel face face-1">
    <span class="block"></span>
    <span class="brand"><i class="mark"></i>Lorvinta</span>
    <div class="range">Capilla<sup>®</sup></div>
    <div class="name">Collagen</div>
    <span class="rule"></span>
    <div class="lead">Helps in Maintaining</div>
    <div class="claim">Healthy and Strong Hair</div>
    <div class="ingr">Hydrolyzed Collagen, Calcium,<br>Zinc, Iron, Betacarotene &amp; B Vitamins</div>
    <div class="weight">(7 sachets of 17 g)<br>Net weight: 119 g</div>
    <div class="band"><div class="format">POWDER IN SACHETS<span>Food Supplement</span></div><div class="count">7 Sachets</div></div>
  </div>

  <div class="panel side side-a">
    <p><b>Capilla Collagen</b> is a daily blend of collagen peptides with nutrients for hair.</p>
    <table class="comp"><caption>Composition</caption>
      <tr><th>Ingredients</th><th>Per Sachet</th></tr>
      <tr><td>Collagen</td><td>10000 mg</td></tr>
      <tr><td>Zinc</td><td>10 mg</td></tr>
      <tr><td>Iron</td><td>14 mg</td></tr>
    </table>
    <p><b>Ingredients:</b> Bovine Collagen, Zinc, Iron, B Vitamins, Flavour.</p>
    <div class="foot"><span class="brand"><i class="mark"></i>Lorvinta</span><small>www.lorvinta.com</small></div>
  </div>

  <div class="panel face face-2">
    <span class="block"></span>
    <span class="brand"><i class="mark"></i>Lorvinta</span>
    <div class="range">Capilla<sup>®</sup></div>
    <div class="name">Collagen</div>
    <span class="rule"></span>
    <div class="lead">Helps in Maintaining</div>
    <div class="claim">Healthy and Strong Hair</div>
    <div class="ingr">Hydrolyzed Collagen, Calcium,<br>Zinc, Iron, Betacarotene &amp; B Vitamins</div>
    <div class="weight">(7 sachets of 17 g)<br>Net weight: 119 g</div>
    <div class="band"><div class="format">POWDER IN SACHETS<span>Food Supplement</span></div><div class="count">7 Sachets</div></div>
  </div>

  <div class="panel bottom">
    <span class="brand"><i class="mark"></i>Lorvinta</span>
    <div class="batch">Batch No.:<br>MFG. Date<br>EXP. Date</div>
    <div class="maker">Velmora S.r.l. Via Orsini 12<br>20121 Milano (MI) - Italy</div>
  </div>

  <div class="panel side side-b">
    <h4>Directions for use:</h4>
    <ul><li>For adults only.</li><li>Take 1 sachet per day, or as directed by the healthcare provider.</li><li>Dissolve the sachet into a glass of water (250 ml).</li></ul>
    <h4>Precautions:</h4>
    <ul><li>Do not exceed the recommended daily dose.</li><li>Not a substitute for a varied, balanced diet.</li><li>Do not use after the expiry date.</li></ul>
    <h4>Storage conditions:</h4>
    <ul><li>Store in a cool (&lt;25°C) and dry place.</li><li>Keep out of reach of children.</li></ul>
  </div>
</section>

<!-- ========== ARTIVA ========== -->
<section class="dieline dieline--joints" aria-label="Artiva Collagen carton dieline">
  <div class="flap glue-left"></div><div class="flap glue-right"></div>
  <div class="flap tuck tuck-a"></div><div class="flap tuck tuck-b"></div><div class="flap tuck tuck-c"></div><div class="flap tuck tuck-d"></div>
  <div class="panel lid"><span class="rule"></span><span class="brand"><i class="mark"></i>Lorvinta</span></div>

  <div class="panel face face-1">
    <span class="block"></span>
    <span class="brand"><i class="mark"></i>Lorvinta</span>
    <div class="range">Artiva<sup>®</sup></div>
    <div class="name">Collagen</div>
    <span class="rule"></span>
    <div class="lead">Promotes</div>
    <div class="claim">Joints Flexibility</div>
    <div class="ingr">Hydrolyzed Collagen, Glucosamine, Chondroitin,<br>Hyaluronic Acid, Vitamin D3 &amp; Selen</div>
    <div class="weight">(7 sachets of 15 g)<br>Net weight: 105 g</div>
    <div class="band"><div class="format">POWDER IN SACHETS<span>Food Supplement</span></div><div class="count">7 Sachets</div></div>
  </div>

  <div class="panel side side-a">
    <p><b>Artiva Collagen</b> is a daily blend of collagen peptides with nutrients for joints.</p>
    <table class="comp"><caption>Composition</caption>
      <tr><th>Ingredients</th><th>Per Sachet</th></tr>
      <tr><td>Collagen</td><td>10000 mg</td></tr>
      <tr><td>Glucosamine</td><td>500 mg</td></tr>
      <tr><td>Vitamin D3</td><td>5 µg</td></tr>
    </table>
    <p><b>Ingredients:</b> Bovine Collagen, Glucosamine, Chondroitin, Flavour.</p>
    <div class="foot"><span class="brand"><i class="mark"></i>Lorvinta</span><small>www.lorvinta.com</small></div>
  </div>

  <div class="panel face face-2">
    <span class="block"></span>
    <span class="brand"><i class="mark"></i>Lorvinta</span>
    <div class="range">Artiva<sup>®</sup></div>
    <div class="name">Collagen</div>
    <span class="rule"></span>
    <div class="lead">Promotes</div>
    <div class="claim">Joints Flexibility</div>
    <div class="ingr">Hydrolyzed Collagen, Glucosamine, Chondroitin,<br>Hyaluronic Acid, Vitamin D3 &amp; Selen</div>
    <div class="weight">(7 sachets of 15 g)<br>Net weight: 105 g</div>
    <div class="band"><div class="format">POWDER IN SACHETS<span>Food Supplement</span></div><div class="count">7 Sachets</div></div>
  </div>

  <div class="panel bottom">
    <span class="brand"><i class="mark"></i>Lorvinta</span>
    <div class="batch">Batch No.:<br>MFG. Date<br>EXP. Date</div>
    <div class="maker">Velmora S.r.l. Via Orsini 12<br>20121 Milano (MI) - Italy</div>
  </div>

  <div class="panel side side-b">
    <h4>Directions for use:</h4>
    <ul><li>For adults only.</li><li>Take 1 sachet per day, or as directed by the healthcare provider.</li><li>Dissolve the sachet into a glass of water (250 ml).</li></ul>
    <h4>Precautions:</h4>
    <ul><li>Do not exceed the recommended daily dose.</li><li>Not a substitute for a varied, balanced diet.</li><li>Do not use after the expiry date.</li></ul>
    <h4>Storage conditions:</h4>
    <ul><li>Store in a cool (&lt;25°C) and dry place.</li><li>Keep out of reach of children.</li></ul>
  </div>
</section>

</body>
</html>
```